Water Filtration Company needs a business card design using our existing logo/colours!

We design and manufacture and export specialised water filtration equipment. Our equipment will take unclean dirty water and filters to safe clean drinkable water.
We would like to see designs using our existing logo and colours (see attached "Palette") that represents clean safe drinking water (fresh, clean designs but still professional and modern). Our customers are other businesses who supply water filtration equipment, governments, and private individuals.
BUSINESS CARD DETAILS (Common details):
Tel: + 61 7 55 914 372
www: brenvalegroup.com.au
Address: 3/41 Corbett Lane
Kellow Ridge NSW 2517 Australia
(please include the word Australia as we are an international company)
Must include: COMMERCIAL WATER FILTRATION EQUIPMENT
NAME NO 1:
Dennis Harper
General Manager
Mobile: +61 418 27 93 40
Email: dennis@brenvalegroup.com.au
NAME NO. 2:
Karen Poe
Business Manager
Mobile: +61 416 572 814
Email: karen@brenvalegroup.com.au
Must Have:
1) PRINT READY IN .AI & .PDF FORMATS
2) Also saved in file format .ai (Adobe Illustrator - compatible with CS4)
3) Use existing LOGO & COLOURS: Please use our logo (see attached file)
4) FONTS: we have used Avenir & Helvetica in the past but are open to other font types for the address etc.
Thank you!

```html
<!DOCTYPE html>
<html lang="en">
<head>
<meta charset="utf-8">
<title>Brenvale Group – Business Cards</title>
<link rel="stylesheet" href="https://fonts.googleapis.com/css2?family=Arimo:wght@400;700&family=Michroma&display=swap">
<style>
  :root {
    --teal: #3bb8c6;
    --brand-blue: #1f6394;
    --ink: #1d1d1f;
    --paper: #ffffff;
    --backdrop: #ececec;
    --card-w: 470px;
    --card-h: 290px;
  }
  * { box-sizing: border-box; margin: 0; padding: 0; }
  html, body { width: 1037px; height: 1200px; overflow: hidden; }
  body {
    background: var(--backdrop);
    font-family: "Arimo", Arial, sans-serif;
    color: var(--ink);
    position: relative;
  }
  .card {
    position: absolute;
    width: var(--card-w);
    height: var(--card-h);
    background: var(--paper);
    overflow: hidden;
    box-shadow: 0 6px 18px rgba(0,0,0,0.16);
  }
  .card--dennis { left: 33px; top: 270px; }
  .card--karen { left: 534px; top: 270px; }
  .card--back { left: 283px; top: 640px; }

  .brand-name {
    position: absolute;
    display: flex;
    align-items: center;
    gap: 8px;
    font-family: "Arimo", Arial, sans-serif;
    font-weight: 700;
    color: var(--brand-blue);
    font-size: 26px;
    letter-spacing: -0.5px;
    line-height: 1;
  }
  .brand-name .brand-dot {
    width: 12px; height: 12px; border-radius: 50%;
    background: var(--brand-blue);
  }
  .card-front .brand-name { left: 36px; top: 52px; }

  .person {
    position: absolute;
    left: 306px; top: 60px;
  }
  .person-name { font-size: 23px; font-weight: 400; color: var(--ink); line-height: 1.1; }
  .person-title { font-size: 14px; color: var(--teal); margin-top: 2px; }

  .contact-band {
    position: absolute;
    left: 0; right: 0; bottom: 0;
    height: 98px;
    background: var(--teal);
    padding: 34px 30px 0;
  }
  .contact-list { list-style: none; }
  .contact-list li {
    display: flex; align-items: center; gap: 14px;
    font-size: 12.5px; line-height: 1; margin-bottom: 10px; color: var(--ink);
  }
  .icon { width: 12px; height: 12px; flex: none; }

  .tagline {
    position: absolute; left: 0; right: 0; top: 48px;
    text-align: center;
    font-family: "Michroma", "Arimo", sans-serif;
    font-size: 14px; letter-spacing: 2.6px; line-height: 30px; color: var(--ink);
  }
  .tagline .highlight { color: var(--brand-blue); }

  .back-contact {
    position: absolute; left: 32px; top: 150px; list-style: none;
  }
  .back-contact li {
    display: flex; align-items: flex-start; gap: 14px;
    font-size: 11.5px; line-height: 15px; margin-bottom: 7px; color: var(--ink);
  }
  .back-contact .icon { margin-top: 1px; fill: var(--brand-blue); }
  .card-back .brand-name { right: 30px; top: 180px; font-size: 22px; }

  .footer-strip { position: absolute; left: 0; bottom: 0; width: 100%; height: 20px; }
</style>
</head>
<body>

  <svg width="0" height="0" style="position:absolute" aria-hidden="true">
    <defs>
      <symbol id="icon-globe" viewBox="0 0 12 12">
        <circle cx="6" cy="6" r="5" fill="none" stroke="currentColor" stroke-width="1"/>
        <ellipse cx="6" cy="6" rx="2.2" ry="5" fill="none" stroke="currentColor" stroke-width="0.9"/>
        <line x1="1" y1="6" x2="11" y2="6" stroke="currentColor" stroke-width="0.9"/>
        <line x1="2" y1="3.5" x2="10" y2="3.5" stroke="currentColor" stroke-width="0.7"/>
        <line x1="2" y1="8.5" x2="10" y2="8.5" stroke="currentColor" stroke-width="0.7"/>
      </symbol>
      <symbol id="icon-phone" viewBox="0 0 12 12">
        <rect x="3" y="0.5" width="6" height="11" rx="1" fill="none" stroke="currentColor" stroke-width="1.1"/>
        <line x1="5" y1="9.6" x2="7" y2="9.6" stroke="currentColor" stroke-width="0.9"/>
      </symbol>
      <symbol id="icon-pin" viewBox="0 0 12 12">
        <path d="M6 0.5a3.8 3.8 0 0 0-3.8 3.8C2.2 7 6 11.5 6 11.5S9.8 7 9.8 4.3A3.8 3.8 0 0 0 6 0.5z" fill="currentColor"/>
        <circle cx="6" cy="4.3" r="1.3" fill="#fff"/>
      </symbol>
    </defs>
  </svg>

  <!-- Front: Dennis Harper -->
  <section class="card card-front card--dennis">
    <div class="brand-name"><span class="brand-dot"></span>Brenvale Group</div>
    <div class="person">
      <p class="person-name">Dennis Harper</p>
      <p class="person-title">General Manager</p>
    </div>
    <div class="contact-band">
      <ul class="contact-list">
        <li><svg class="icon"><use href="#icon-globe"/></svg>dennis@brenvalegroup.com.au</li>
        <li><svg class="icon"><use href="#icon-phone"/></svg>+61 418 27 93 40</li>
      </ul>
    </div>
  </section>

  <!-- Front: Karen Poe -->
  <section class="card card-front card--karen">
    <div class="brand-name"><span class="brand-dot"></span>Brenvale Group</div>
    <div class="person">
      <p class="person-name">Karen Poe</p>
      <p class="person-title">Business Manager</p>
    </div>
    <div class="contact-band">
      <ul class="contact-list">
        <li><svg class="icon"><use href="#icon-globe"/></svg>karen@brenvalegroup.com.au</li>
        <li><svg class="icon"><use href="#icon-phone"/></svg>+61 416 572 814</li>
      </ul>
    </div>
  </section>

  <!-- Back: shared -->
  <section class="card card-back card--back">
    <h1 class="tagline">COMMERCIAL <span class="highlight">WATER</span> FILTRATION<br>EQUIPMENT</h1>
    <ul class="back-contact">
      <li><svg class="icon"><use href="#icon-pin"/></svg><span>3/41 Corbett Lane<br>Kellow Ridge NSW 2517 Australia</span></li>
      <li><svg class="icon" style="color:var(--brand-blue)"><use href="#icon-globe"/></svg><span>www.brenvalegroup.com.au</span></li>
      <li><svg class="icon" style="color:var(--brand-blue)"><use href="#icon-phone"/></svg><span>+ 61 7 55 914 372</span></li>
    </ul>
    <div class="brand-name"><span class="brand-dot"></span>Brenvale Group</div>
    <svg class="footer-strip" viewBox="0 0 470 20" preserveAspectRatio="none" aria-hidden="true">
      <rect x="0" y="6" width="470" height="14" fill="var(--teal)"/>
      <polygon points="218,20 224,6 228,6 222,20" fill="#fff"/>
      <polygon points="232,20 238,6 242,6 236,20" fill="#fff"/>
    </svg>
  </section>

</body>
</html>
```